Vehicles Brochure Diagram

Task Outline
Create diagrams for our new vehicles brochures

Task Description

Who are we:
KTW is New Zealand's largest Business Group Buying organisation, helping organisations nationwide reduce their running costs. We offer members the best deals from over 100 Contracted Suppliers, anything from vehicles, stationery to electronics and coffee.

The project:
We need 2 diagrams to illustrate the benefits of our vehicle services. The diagram will be used in our brochures (example attached)

1. A Diagram illustrating/explaining the elements that are involved in purchasing a new car & how our service ties it all together to provide the best solution.
- Please see the Diagram 1 PDF for a rough wireframe of the elements involved

2. Another small diagram inserted on an separate page to demonstrate how our services can increase safety & profit and reduce costs & risks (PDF: Diagram 2 Details)

The design needs to be clean, clear and simple that it’s easy to understand within a few seconds of looking at it. Feel free to explore with different elements in the realm of infographics, flowcharts & diagrams to best communicate the idea visually.
Updates

Just thought I’ll share some of the feedback we’re giving tosubmissions that have been coming through to help with new submissions

-Challenge & be creative about the ways you demonstratethe elements

-We don’t want to see your design replicating the ones that isdrawn. The purpose of it is only to provide you with the content in context

-We can’t emphasis enough that the style pdf is only areference and not the look you should imitate. 

If you have any question please feel free to contact me.Looking forward to see your designs!

Project Deadline Extended
Reason: We're keen to see more approaches & creative ways of interpreting the content rather than a standard cycle diagram. Entries so far have been good but quite literal, we will provide feedback to help steer it in the right direction.

Target Market(s)

Business professionals, Decision makers on a corporate level & prospects.

Industry/Entity Type

Electronics

Requirements
Must have

• Likes – simple, clean & clear, uncluttered

Dislikes – Overcrowded images, text, & colours. Overly expressive typeface. Please no literal illustration of our sketches or colored version of our sketch.

Font: -Myriad Pro

Colour: Please refer to the color palette in the ‘Diagram Color & Style’ PDF

The brochures are attached with content to provide context that might inform the design better,

Dimensions & the amount of space you have to work with will also be highlighted

```html
<!DOCTYPE html>
<html lang="en">
<head>
<meta charset="utf-8">
<title>Vehicle Purchase Diagram</title>
<link rel="stylesheet" href="https://fonts.googleapis.com/css2?family=Source+Sans+3:wght@400;600;700&display=swap">
<style>
  :root {
    --bg: #ffffff;
    --orange-light: #f9b770;
    --orange: #f28a1f;
    --orange-edge: #fbc891;
    --blue-pale: #c4e2f6;
    --blue-mid: #6aaedf;
    --blue-deep: #3d86c6;
    --ring-light: #79bce9;
    --ring-dark: #2a6fb8;
    --white: #ffffff;
  }
  html, body {
    margin: 0;
    padding: 0;
    width: 1200px;
    height: 900px;
    overflow: hidden;
    background: var(--bg);
  }
  .canvas {
    position: relative;
    width: 1200px;
    height: 900px;
    font-family: "Source Sans 3", "Myriad Pro", sans-serif;
    color: var(--white);
  }
  .diagram-art {
    position: absolute;
    left: 0;
    top: 0;
  }
  .hub-title {
    position: absolute;
    left: 405px;
    top: 252px;
    width: 400px;
    margin: 0;
    text-align: center;
    font-weight: 600;
    font-size: 45px;
    line-height: 58px;
  }
  .vehicle-icon {
    position: absolute;
    left: 368px;
    top: 385px;
    width: 428px;
    height: 192px;
    border-radius: 24px;
    background: linear-gradient(180deg, rgba(255,255,255,0.55), rgba(255,255,255,0.25));
  }
  .stage {
    position: absolute;
    box-sizing: border-box;
    border-radius: 16px;
    border: 2px solid var(--orange-edge);
    background: linear-gradient(180deg, var(--orange-light) 0%, var(--orange) 100%);
    box-shadow: 0 3px 6px rgba(0,0,0,0.12);
    padding: 22px 30px;
  }
  .stage-title {
    margin: 0;
    font-weight: 600;
    font-size: 32px;
    line-height: 38px;
  }
  .stage-list {
    list-style: none;
    margin: 10px 0 0 10px;
    padding: 0;
    display: grid;
    grid-template-columns: auto auto;
    column-gap: 28px;
    row-gap: 4px;
    font-size: 21px;
    line-height: 27px;
    justify-content: start;
  }
  .stage-list li::before {
    content: "\2022";
    margin-right: 10px;
  }
  .stage--headline {
    left: 350px; top: 52px; width: 495px; height: 140px;
    display: flex; align-items: center; justify-content: center;
    text-align: center;
  }
  .stage--headline .stage-title { font-size: 34px; line-height: 40px; }
  .stage--run { left: 818px; top: 267px; width: 322px; height: 171px; }
  .stage--disposal { left: 60px; top: 264px; width: 323px; height: 174px; padding-top: 30px; }
  .stage--company { left: 145px; top: 640px; width: 317px; height: 178px; padding-top: 18px; }
  .stage--company .stage-title { line-height: 34px; }
  .stage--company .stage-list { margin-top: 8px; }
  .stage--manage { left: 725px; top: 640px; width: 321px; height: 178px; }
</style>
</head>
<body>
<div class="canvas">
  <svg class="diagram-art" width="1200" height="900" viewBox="0 0 1200 900">
    <defs>
      <linearGradient id="hubFill" x1="0" y1="0" x2="1" y2="1">
        <stop offset="0" stop-color="var(--blue-pale)"/>
        <stop offset="0.5" stop-color="var(--blue-mid)"/>
        <stop offset="1" stop-color="var(--blue-deep)"/>
      </linearGradient>
      <linearGradient id="ringStroke" x1="0" y1="0" x2="1" y2="1">
        <stop offset="0" stop-color="var(--ring-light)"/>
        <stop offset="1" stop-color="var(--ring-dark)"/>
      </linearGradient>
      <marker id="arrowHead" viewBox="0 0 20 20" refX="14" refY="10"
              markerWidth="56" markerHeight="56" markerUnits="userSpaceOnUse"
              orient="auto-start-reverse">
        <path d="M0,0 L20,10 L0,20 Z" fill="var(--ring-dark)"/>
      </marker>
    </defs>

    <circle class="hub" cx="605" cy="432" r="322" fill="url(#hubFill)"/>
    <circle class="cycle-ring" cx="605" cy="432" r="330" fill="none"
            stroke="url(#ringStroke)" stroke-width="26"/>

    <g class="cycle-arrows" fill="none" stroke="var(--ring-dark)" stroke-width="26">
      <path d="M718,122 A330,330 0 0 1 875,243" marker-end="url(#arrowHead)"/>
      <path d="M935,444 A330,330 0 0 1 865,635" marker-start="url(#arrowHead)" marker-end="url(#arrowHead)"/>
      <path d="M723,740 A330,330 0 0 1 471,733" marker-start="url(#arrowHead)" marker-end="url(#arrowHead)"/>
      <path d="M345,635 A330,330 0 0 1 276,449" marker-start="url(#arrowHead)" marker-end="url(#arrowHead)"/>
    </g>
  </svg>

  <h1 class="hub-title">Best fit<br>for purpose</h1>
  <div class="vehicle-icon" role="img" aria-label="White icon of a car beside a fuel pump"></div>

  <div class="stage stage--headline">
    <h2 class="stage-title">There is more to a vehicle purchase than just the PRICE</h2>
  </div>

  <div class="stage stage--run">
    <h2 class="stage-title">Cost to Run</h2>
    <ul class="stage-list">
      <li>Fuel</li><li>Rego</li>
      <li>Tyres</li><li>RoC</li>
    </ul>
  </div>

  <div class="stage stage--disposal">
    <h2 class="stage-title">End of Life<br>Disposal Costs</h2>
  </div>

  <div class="stage stage--company">
    <h2 class="stage-title">Your Company<br>Requirements</h2>
    <ul class="stage-list">
      <li>Sustainability</li><li>Safty</li>
      <li>Specifications</li>
    </ul>
  </div>

  <div class="stage stage--manage">
    <h2 class="stage-title">Cost to Manage</h2>
    <ul class="stage-list">
      <li>Lease</li><li>Finance</li>
      <li>Insurance</li><li style="list-style:none">&amp; Tax</li>
    </ul>
  </div>
</div>
</body>
</html>
```